3 Business Card designs for a company with multiple services

We are a company that has 3 main services:

1) Security - CCTV & Alarm Sepcialists
2) Broadcast - Broadcast Sales and Technical Services
3) Distribution - Quality Products, Quality Service

The broadcast service is for Video Broadcast.

I will include our logos for each service.

I would like to also create a business card design for 7QK in general (see main logo).

Each card will be two-sided. On the front I would think it would include Logo, Name, Posistion and Mobile (and possibly email). And possibly our main number (which may be something like 1800 639 415)

On the back it MUST include a "lined" section to be able to write short quotes / prices.

Then include more details like Phone: 1800 639 415 Fax: 1800 639 412 Postal: PO Box 731, Tallowen, QLD Australia 4290 Website: www.7qk.com.au

We would like a fresh, inovative card design with that "wow check this out" feel about it.

Look forward to seeing what you can do! :)

Corey

Industry/Entity Type

Business

Requirements
Must have
• Quote section on the back!
Editable files.

```html
<!DOCTYPE html>
<html lang="en">
<head>
<meta charset="utf-8">
<title>7QK Business Cards</title>
<link rel="stylesheet" href="https://fonts.googleapis.com/css2?family=Arimo:wght@400;700&display=swap">
<style>
  :root {
    --bg: #d9d9d9;
    --header-dark: #1c1c1c;
    --header-mid: #3a3a3a;
    --white: #ffffff;
    --security: #8a8c90;
    --security-light: #b4b6ba;
    --broadcast: #d4822a;
    --broadcast-light: #e39a45;
    --distribution: #22409a;
    --distribution-light: #2f55b8;
    --black-card: #050505;
    --band: #3b3b3b;
    --ink: #1a1a1a;
    --muted: #8a8a8a;
    --rule: #555555;
    --lock-red: #d42a22;
    --camera-gold: #e0a21c;
    --globe-blue: #2a6fc4;
    --lock-grey: #a8a8a8;
  }
  * { box-sizing: border-box; margin: 0; padding: 0; }
  html, body { width: 1200px; height: 900px; overflow: hidden; }
  body {
    background: var(--bg);
    font-family: "Arimo", Arial, sans-serif;
    position: relative;
  }
  .card {
    position: absolute;
    overflow: hidden;
    box-shadow: 0 6px 18px rgba(0,0,0,0.25);
  }

  /* Vertical service cards */
  .service-card { width: 240px; height: 393px; top: 60px; }
  .service-card--security { left: 180px; background: linear-gradient(180deg, var(--security-light), var(--security)); }
  .service-card--broadcast { left: 480px; background: linear-gradient(180deg, var(--broadcast-light), var(--broadcast)); }
  .service-card--distribution { left: 780px; background: linear-gradient(180deg, var(--distribution-light), var(--distribution)); }

  .service-header {
    height: 96px;
    background: linear-gradient(180deg, var(--header-mid), var(--header-dark));
    position: relative;
  }
  .service-icon {
    position: absolute; left: 12px; top: 12px;
    width: 50px; height: 50px; border-radius: 6px;
  }
  .service-card--security .service-icon { background: var(--lock-red); }
  .service-card--broadcast .service-icon { background: var(--camera-gold); }
  .service-card--distribution .service-icon { background: radial-gradient(circle at 40% 40%, #ffd24a, var(--globe-blue)); border-radius: 50%; }

  .brand-name {
    position: absolute; right: 16px; top: 10px;
    font-weight: 700; font-size: 40px; letter-spacing: 14px;
    color: var(--white);
  }
  .service-label {
    position: absolute; right: 14px; bottom: 10px;
    font-weight: 700; font-size: 16px; letter-spacing: 4px;
    color: var(--white);
  }
  .person {
    position: absolute; left: 0; right: 0; bottom: 34px;
    text-align: center; color: var(--white); font-size: 15px; line-height: 1.6;
  }

  /* Horizontal combined front */
  .front-card {
    left: 150px; top: 520px; width: 420px; height: 256px;
    background: var(--black-card); color: var(--white);
  }
  .front-header {
    height: 86px; position: relative;
    background: linear-gradient(180deg, #4a4a4a, #2a2a2a);
  }
  .front-icons { position: absolute; left: 16px; top: 20px; display: flex; gap: 14px; }
  .front-icon { width: 44px; height: 44px; border-radius: 6px; }
  .front-icon--security { background: var(--lock-grey); }
  .front-icon--broadcast { background: var(--camera-gold); }
  .front-icon--distribution { background: radial-gradient(circle at 40% 40%, #8cc4ff, var(--globe-blue)); border-radius: 50%; }
  .front-card .brand-name { top: 14px; font-size: 46px; }
  .front-band {
    height: 34px; background: linear-gradient(180deg, #555, var(--band));
    display: flex; align-items: center; justify-content: center;
    font-weight: 700; font-size: 17px; letter-spacing: 2px;
  }
  .front-person { position: absolute; left: 16px; bottom: 22px; font-size: 15px; line-height: 1.6; }
  .front-contact { position: absolute; right: 16px; bottom: 22px; font-size: 15px; line-height: 1.6; text-align: right; }

  /* Appointment back */
  .back-card {
    left: 630px; top: 520px; width: 420px; height: 256px;
    background: var(--white); color: var(--ink);
    padding: 14px 22px;
  }
  .back-title { text-align: center; font-weight: 700; font-size: 20px; letter-spacing: 4px; margin-bottom: 14px; }
  .field { display: flex; align-items: flex-end; font-size: 18px; height: 28px; }
  .field-label { width: 84px; }
  .field-line { flex: 1; border-bottom: 1.5px solid var(--rule); margin-bottom: 4px; }
  .back-note { margin-top: 12px; text-align: center; color: var(--muted); font-size: 13px; line-height: 1.35; }
  .back-contact { margin-top: 12px; text-align: center; font-size: 13px; line-height: 1.45; }
</style>
</head>
<body>

  <section class="card service-card service-card--security">
    <div class="service-header">
      <div class="service-icon" role="img" aria-label="Security padlock icon"></div>
      <div class="brand-name">7QK</div>
      <div class="service-label">SECURITY</div>
    </div>
    <div class="person">Persons Name<br>DIRECTOR</div>
  </section>

  <section class="card service-card service-card--broadcast">
    <div class="service-header">
      <div class="service-icon" role="img" aria-label="Broadcast camera icon"></div>
      <div class="brand-name">7QK</div>
      <div class="service-label">BROADCAST</div>
    </div>
    <div class="person">Persons Name<br>DIRECTOR</div>
  </section>

  <section class="card service-card service-card--distribution">
    <div class="service-header">
      <div class="service-icon" role="img" aria-label="Distribution globe icon"></div>
      <div class="brand-name">7QK</div>
      <div class="service-label">DISTRIBUTION</div>
    </div>
    <div class="person">Persons Name<br>DIRECTOR</div>
  </section>

  <section class="card front-card">
    <div class="front-header">
      <div class="front-icons">
        <div class="front-icon front-icon--security" role="img" aria-label="Security padlock icon"></div>
        <div class="front-icon front-icon--broadcast" role="img" aria-label="Broadcast camera icon"></div>
        <div class="front-icon front-icon--distribution" role="img" aria-label="Distribution globe icon"></div>
      </div>
      <div class="brand-name">7QK</div>
    </div>
    <div class="front-band">SECURITY - BROADCAST - DISTRIBUTION</div>
    <div class="front-person">Persons Name<br>DIRECTOR</div>
    <div class="front-contact">04123567890<br>Name@7qk.com.au</div>
  </section>

  <section class="card back-card">
    <h2 class="back-title">APPOINTMENT</h2>
    <div class="field"><span class="field-label">DATE :</span><span class="field-line"></span></div>
    <div class="field"><span class="field-label">TIME:</span><span class="field-line"></span></div>
    <div class="field"><span class="field-label">PLACE:</span><span class="field-line"></span></div>
    <p class="back-note">If you are unable to attend the appointment please notify me<br>as soon as possible.</p>
    <p class="back-contact">T 1800 639 415 &nbsp;F 1800 639 412<br>PO Box 731, Tallowen, QLD Australia 4290<br>www.7qk.com.au</p>
  </section>

</body>
</html>
```